Bolvarin Incorporated

Bolvarin is a business that provides consulting, and manages and supplies trades persons in the construction and heavy industries sector. We build, do maintenance, install machinery, and can manage projects or jobs. Would like or prefer more clean, classic designs. Blacks/greys, but open to almost anything.

Target Market(s)

Industrial/Construction/Manufacturing

Industry/Entity Type

Construction Company

Contact Information for Business Card

Clean, business name on the front, possibly have the details on the back, but open to any ideas.

Logo Text

We currently do not have a slogan, open to ideas

Font styles to use
Serif
Sans Serif

Colors

Designer to choose colors to be used in the design.

Requirements
Should not have
• the oval is not my logo, was just an idea. please don't send 20 designs with the oval

```html
<!DOCTYPE html>
<html lang="en">
<head>
<meta charset="utf-8">
<title>Bolvarin Incorporated – Business Card</title>
<link rel="stylesheet" href="https://fonts.googleapis.com/css2?family=Exo+2:wght@300;400&display=swap">
<style>
  :root {
    --navy: #1c212c;
    --orange: #e0792b;
    --sky: #6aaee0;
    --ink: #1e2430;
    --paper: #ffffff;
    --sans: "Exo 2", sans-serif;
  }
  html, body {
    margin: 0;
    padding: 0;
    overflow: hidden;
    background: var(--paper);
  }
  .card {
    position: relative;
    width: 1200px;
    height: 857px;
    overflow: hidden;
    background: var(--paper);
    font-family: var(--sans);
    color: var(--ink);
  }
  .header-bands {
    position: absolute;
    left: 0;
    top: 0;
    width: 1200px;
    height: 857px;
  }
  .brand {
    position: absolute;
    left: 80px;
    top: 60px;
    color: var(--paper);
    font-family: var(--sans);
    font-weight: 400;
    line-height: 1;
  }
  .brand-name {
    display: block;
    font-size: 84px;
    letter-spacing: 1px;
  }
  .brand-suffix {
    display: block;
    font-size: 15px;
    letter-spacing: 1px;
    text-align: right;
    margin-top: 4px;
  }
  .person {
    position: absolute;
    left: 112px;
    top: 553px;
    line-height: 1;
  }
  .person-name {
    margin: 0;
    font-size: 60px;
    font-weight: 400;
  }
  .person-role {
    margin: 8px 0 0 4px;
    font-size: 40px;
    font-weight: 300;
  }
  .divider {
    position: absolute;
    left: 641px;
    top: 386px;
    width: 2px;
    height: 272px;
    background: var(--orange);
  }
  .contact-icon {
    position: absolute;
    left: 582px;
    width: 40px;
    height: 40px;
    fill: none;
    stroke: var(--orange);
    stroke-width: 1.8;
    stroke-linejoin: round;
    stroke-linecap: round;
  }
  .icon-mail  { top: 391px; }
  .icon-phone { top: 482px; }
  .icon-home  { top: 570px; }
  .contact-line {
    position: absolute;
    left: 689px;
    margin: 0;
    font-size: 35px;
    font-weight: 300;
    line-height: 1;
    font-style: normal;
  }
  .contact-email   { top: 391px; }
  .contact-phone   { top: 486px; }
  .contact-address { top: 574px; line-height: 46px; }
</style>
</head>
<body>
  <main class="card">
    <svg class="header-bands" viewBox="0 0 1327 948" preserveAspectRatio="none" aria-hidden="true">
      <polygon fill="var(--orange)" points="0,206 250,298 272,299 0,238"/>
      <polygon fill="var(--sky)" points="240,297 1327,182 1327,218 268,299"/>
      <polygon fill="var(--navy)" points="0,0 1327,0 1327,182 245,297 0,206"/>
    </svg>

    <div class="brand">
      <span class="brand-name">Bolvarin</span>
      <span class="brand-suffix">INCORPORATED</span>
    </div>

    <div class="person">
      <h1 class="person-name">Daniel Harper</h1>
      <p class="person-role">Operations Manager</p>
    </div>

    <div class="divider"></div>

    <svg class="contact-icon icon-mail" viewBox="0 0 40 40" aria-hidden="true">
      <path d="M3 6 L37 5 L24 35 L19 21 Z M19 21 L37 5"/>
    </svg>
    <svg class="contact-icon icon-phone" viewBox="0 0 40 40" aria-hidden="true">
      <path d="M9 4 L15 12 L11 17 C13 23 17 27 23 30 L28 26 L36 32 C33 37 28 38 23 36 C14 32 7 25 4 15 C3 10 5 6 9 4 Z"/>
    </svg>
    <svg class="contact-icon icon-home" viewBox="0 0 40 40" aria-hidden="true">
      <path d="M3 19 L20 4 L37 19 M7 16 V36 H16 V25 H24 V36 H33 V16"/>
    </svg>

    <p class="contact-line contact-email">danielharper@bolvarin.com</p>
    <p class="contact-line contact-phone">555-204-318-6</p>
    <address class="contact-line contact-address">4182 Larkspur Rd.<br>Dunmore, PA 18512</address>
  </main>
</body>
</html>
```